Business Card Design for Brackfell Studios

Design the layout for a two-sided business card incorporating the logo design produced through Pixel Harbor by tomekdurish earlier this year. Design to be created as per specifications for standard size cards produced by Pryntle.com. Art work dimensions to be restricted to 3.66" x 2.16"

Front of card to include Brackfell Studios Logo and name and contact information. Back side to include logo only.

Target Market(s)

Photography clients.

Industry/Entity Type

Business

Contact Information for Business Card

Derek Hollis, Photographer
23-815 Osprey Hill Drive
Yellowknife, NT X0E 2K7

867-555-3182

derek@brackfellstudios.example

www.brackfellstudios.example

Font styles to use
Serif

Requirements
Must have
• Logo, name, contact information, email and website.
• Use colours from original logo design.
Nice to have
• I'm thinking a black background, but I'm open to other ideas.

```html
<!DOCTYPE html>
<html lang="en">
<head>
<meta charset="utf-8">
<title>Brackfell Studios – Business Card</title>
<link href="https://fonts.googleapis.com/css2?family=Cinzel:wght@400;500&family=Open+Sans:wght@300;400&display=swap" rel="stylesheet">
<style>
  :root {
    --backdrop: #929397;
    --card-black: #050506;
    --band-dark: #1b1b1d;
    --band-light: #2c2c2f;
    --gold: #c9a24a;
    --teal: #2a9fb0;
    --white: #ffffff;
    --text-soft: #e6e6e6;
  }
  * { margin: 0; padding: 0; box-sizing: border-box; }
  html, body { width: 1200px; height: 1000px; overflow: hidden; background: var(--backdrop); }
  .canvas { position: relative; width: 1200px; height: 1000px; }
  .card {
    position: absolute; left: 289px; width: 623px; height: 365px;
    background: var(--card-black); overflow: hidden;
    box-shadow: 4px 6px 8px rgba(0,0,0,0.35);
  }
  .card--front { top: 119px; }
  .card--back { top: 510px; }
  .card-art { position: absolute; inset: 0; width: 623px; height: 365px; }
  .portrait {
    position: absolute; left: 395px; top: 0; width: 228px; height: 340px;
    background: radial-gradient(ellipse 60% 60% at 60% 40%, #6a6a6a 0%, #3e3e3e 45%, #141414 80%, var(--card-black) 100%);
    -webkit-mask-image: linear-gradient(to right, transparent 0%, #000 30%);
            mask-image: linear-gradient(to right, transparent 0%, #000 30%);
  }
  .brand { position: absolute; display: flex; align-items: center; gap: 12px; }
  .brand-mark {
    width: 70px; height: 70px; border-radius: 50%;
    border: 4px solid var(--white); background: var(--card-black);
  }
  .brand-name {
    font-family: "Cinzel", serif; font-weight: 500; font-size: 25px;
    line-height: 1; color: var(--gold); letter-spacing: 0.5px;
  }
  .card--front .brand { left: 39px; top: 38px; }
  .card--back .brand { left: 172px; top: 142px; }
  .holder { position: absolute; left: 52px; top: 126px; }
  .holder-name {
    font-family: "Cinzel", serif; font-weight: 400; font-size: 33px;
    line-height: 1; letter-spacing: 0.5px; color: var(--gold);
  }
  .holder-name .surname { color: var(--teal); }
  .holder-role {
    margin-top: 7px; font-family: "Open Sans", sans-serif; font-weight: 300;
    font-size: 19px; letter-spacing: 1.5px; color: var(--white);
  }
  .contact { position: absolute; left: 50px; top: 237px; list-style: none; }
  .contact-item {
    display: flex; align-items: flex-start; gap: 8px; margin-bottom: 6px;
    font-family: "Open Sans", sans-serif; font-size: 11.5px; line-height: 1.2; color: var(--text-soft);
  }
  .contact-icon { width: 16px; height: 16px; flex: none; }
</style>
</head>
<body>
<div class="canvas">

  <section class="card card--front" aria-label="Card front">
    <div class="portrait" role="img" aria-label="Black and white portrait photograph of the photographer"></div>
    <svg class="card-art" viewBox="0 0 623 365" aria-hidden="true">
      <defs>
        <linearGradient id="frontBand" x1="0" y1="0" x2="0" y2="1">
          <stop offset="0" stop-color="#2e2e31"/>
          <stop offset="1" stop-color="#161618"/>
        </linearGradient>
      </defs>
      <path d="M0 212 C150 196 300 204 420 258 C520 305 565 342 623 360 L623 365 L0 365 Z" fill="url(#frontBand)"/>
      <path d="M0 212 C150 196 300 204 420 258 C520 305 565 342 623 360" fill="none" stroke="#4a4a4e" stroke-width="1.2"/>
    </svg>

    <div class="brand">
      <span class="brand-mark"></span>
      <span class="brand-name">Brackfell Studios</span>
    </div>

    <div class="holder">
      <h1 class="holder-name">Derek <span class="surname">Hollis</span></h1>
      <p class="holder-role">Photographer</p>
    </div>

    <ul class="contact">
      <li class="contact-item">
        <svg class="contact-icon" viewBox="0 0 16 16"><circle cx="8" cy="8" r="8" fill="var(--teal)"/><path d="M5 4.5 L6.5 4 L7.5 6.5 L6.5 7.2 C7 8.4 7.6 9 8.8 9.5 L9.5 8.5 L12 9.5 L11.5 11 C8 11 5 8 5 4.5 Z" fill="#fff"/></svg>
        <span>867-555-3182</span>
      </li>
      <li class="contact-item">
        <svg class="contact-icon" viewBox="0 0 16 16"><circle cx="8" cy="8" r="8" fill="var(--teal)"/><rect x="4" y="5.2" width="8" height="5.6" fill="#fff"/><path d="M4 5.2 L8 8.4 L12 5.2" fill="none" stroke="var(--teal)" stroke-width="0.9"/></svg>
        <span>derek@brackfellstudios.example</span>
      </li>
      <li class="contact-item">
        <svg class="contact-icon" viewBox="0 0 16 16"><circle cx="8" cy="8" r="8" fill="var(--teal)"/><circle cx="8" cy="8" r="4" fill="none" stroke="#fff" stroke-width="1"/><path d="M4 8 H12 M8 4 C6 6 6 10 8 12 M8 4 C10 6 10 10 8 12" fill="none" stroke="#fff" stroke-width="0.8"/></svg>
        <span>www.brackfellstudios.example</span>
      </li>
      <li class="contact-item">
        <svg class="contact-icon" viewBox="0 0 16 16"><circle cx="8" cy="8" r="8" fill="var(--teal)"/><path d="M8 12.5 C6 10 5 8.5 5 7 A3 3 0 0 1 11 7 C11 8.5 10 10 8 12.5 Z" fill="#fff"/><circle cx="8" cy="7" r="1.1" fill="var(--teal)"/></svg>
        <span>23-815 Osprey Hill Drive<br>Yellowknife, NT X0E 2K7</span>
      </li>
    </ul>
  </section>

  <section class="card card--back" aria-label="Card back">
    <svg class="card-art" viewBox="0 0 623 365" aria-hidden="true">
      <defs>
        <linearGradient id="backTop" x1="0" y1="0" x2="0" y2="1">
          <stop offset="0" stop-color="#141416"/>
          <stop offset="1" stop-color="#2c2c2f"/>
        </linearGradient>
        <linearGradient id="backBottom" x1="0" y1="0" x2="0" y2="1">
          <stop offset="0" stop-color="#2e2e31"/>
          <stop offset="1" stop-color="#151517"/>
        </linearGradient>
      </defs>
      <path d="M130 0 C230 30 300 112 623 116 L623 0 Z" fill="url(#backTop)"/>
      <path d="M130 0 C230 30 300 112 623 116" fill="none" stroke="#3f3f43" stroke-width="1.2"/>
      <path d="M0 238 C190 222 330 236 470 315 C520 342 560 358 600 365 L0 365 Z" fill="url(#backBottom)"/>
      <path d="M0 238 C190 222 330 236 470 315 C520 342 560 358 600 365" fill="none" stroke="#46464a" stroke-width="1.2"/>
    </svg>
    <div class="brand">
      <span class="brand-mark"></span>
      <span class="brand-name">Brackfell Studios</span>
    </div>
  </section>

</div>
</body>
</html>
```